Soft furnishing company selling fabrics, curtains, bedlinen craft & haberdashery

We need 4 x home page banners for our website as follows:
Image 1 - to lead customers to our "New season Fabrics" page,
Image 2 - to lead customers to our Ready Made curtains,
Image 3 - to lead customers to our "Polar Bear Bed linen" page
Image 4 - to lead customers to our "Christmas raft Tutorial" page

Banner needs to be 960px wide x 380px 72dpi and optimised for web. should have a little descriptive text for example "Fabulous Fabric. Prints, plains & weaves, view our range of new season furnishing fabrics to buy by the metre" "Instantly update your home with our range of ready made curtains. Available . "Cosy Night In. Snuggle with this Polar Bear Duvet Set. From €20" "" "Let's Get Crafting for Christmas. Download our free Project and tutoirals here. First 3 images need a "shop now" button

website url www.lindenweave.ie

Target Market(s)

Female 25 -45

Industry/Entity Type

It Company

Font styles to use
Serif
Sans Serif

Requirements
Must have
• shop now button on image 1, 2, 3
Should not have
• too much text or clutter

```html
<!DOCTYPE html>
<html lang="en">
<head>
<meta charset="utf-8">
<title>Lindenweave – New Season Fabrics</title>
<link rel="stylesheet" href="https://fonts.googleapis.com/css2?family=Arimo:wght@400&display=swap">
<style>
  :root {
    --cream-light: #fefaea;
    --cream-deep: #f4e3b6;
    --orange: #f7941d;
    --orange-button: #f26f21;
    --orange-border: #f58220;
    --leaf-red: #e0531c;
    --leaf-gold: #f8b133;
    --fabric-rose: #c9a79a;
    --fabric-sage: #a9b9ad;
    --fabric-stone: #b9b3a6;
    --white: #ffffff;
  }
  html, body {
    margin: 0;
    padding: 0;
    overflow: hidden;
  }
  .banner {
    position: relative;
    width: 1200px;
    height: 475px;
    overflow: hidden;
    background: linear-gradient(160deg, var(--cream-light) 0%, var(--cream-deep) 100%);
    font-family: "Arimo", Arial, sans-serif;
  }
  .autumn-leaves {
    position: absolute;
    top: 0;
    right: 0;
    width: 480px;
    height: 380px;
    background: radial-gradient(ellipse at 85% 25%, var(--leaf-red) 0%, var(--orange) 30%, rgba(248, 177, 51, 0.55) 55%, rgba(248, 177, 51, 0) 75%);
  }
  .leaves-top {
    position: absolute;
    top: 0;
    left: 430px;
    width: 260px;
    height: 70px;
    background: radial-gradient(ellipse at 40% 0%, var(--orange) 0%, rgba(248, 177, 51, 0.5) 45%, rgba(248, 177, 51, 0) 75%);
  }
  .fabric-photo {
    position: absolute;
    inset: 0;
  }
  .headline {
    position: absolute;
    top: 136px;
    left: 520px;
    width: 540px;
    margin: 0;
    text-align: center;
    color: var(--orange);
    font-size: 28px;
    line-height: 40px;
    font-weight: 400;
  }
  .shop-now {
    position: absolute;
    left: 715px;
    top: 379px;
    width: 208px;
    height: 55px;
    border-radius: 10px;
    background: var(--orange-button);
    color: var(--white);
    font-size: 30px;
    line-height: 55px;
    text-align: center;
    text-decoration: none;
  }
</style>
</head>
<body>
  <div class="banner">
    <div class="autumn-leaves" role="img" aria-label="Scattered orange and gold autumn maple leaves"></div>
    <div class="leaves-top" role="img" aria-label="Autumn maple leaves along the top edge"></div>

    <svg class="fabric-photo" width="1200" height="475" viewBox="0 0 1200 475">
      <defs>
        <linearGradient id="fabric-tones" x1="0" y1="0" x2="0" y2="1">
          <stop offset="0" stop-color="var(--fabric-rose)"/>
          <stop offset="0.45" stop-color="var(--fabric-sage)"/>
          <stop offset="0.75" stop-color="var(--fabric-stone)"/>
          <stop offset="1" stop-color="#a7855e"/>
        </linearGradient>
      </defs>
      <polygon class="photo-edge" fill="var(--orange-border)"
               points="0,0 443,0 507,165 534,200 522,214 610,475 0,475"/>
      <polygon role="img" aria-label="Stack of folded patterned furnishing fabrics with falling autumn leaves"
               fill="url(#fabric-tones)"
               points="0,0 431,0 495,165 520,200 508,212 598,475 0,475"/>
    </svg>

    <p class="headline">Fabulous Fabric. Prints,<br>plains &amp; weaves, view our<br>range of new season furnishing<br>fabrics to buy by the metre</p>

    <a class="shop-now" href="#">Shop Now</a>
  </div>
</body>
</html>
```